Flyer-Design für Neueröffnung feinKragen
Zielgruppe
Wir bieten Marken Hemden und Accessoires unter anderem von den Herstellern Faltenmeister, Lumira und Veltrano in unserem Ladengeschäft sowie online in unserem Shop.
Unsere Zielgruppe ist der anspruchsvolle Mann, gut gebildet, aufstrebend und modebewusst, das ist das typische Bild unserer Zielgruppe.
Kunden können von uns ein modisches Hemd in hervorragender Qualität und exzellentem Service erwarten.
Aufgabenstellung
Feiern Sie mit uns die
NEU ERÖFFNUNG
Endlich in Oberkochen Markenhemden in großer Auswahl.
Am Samstag, 01. April 09:00-16:00Uhr
20% auf Alles - kein Aprilscherz
www.feinKragen.de
(Texte könne auch verändert werden, außer die Fakten - Neueröffnung - Datum - 20% auf alles)

```html
<!DOCTYPE html>
<html lang="de">
<head>
<meta charset="utf-8">
<title>feinKragen – Neueröffnung</title>
<link href="https://fonts.googleapis.com/css2?family=Archivo+Black&family=Courier+Prime:wght@700&family=Inter:wght@300;400;700&family=Oswald:wght@600&family=Playfair+Display:wght@500&display=swap" rel="stylesheet">
<style>
:root{
  --orange:#ef7d00;
  --ink:#000;
  --plum:#4a2540;
  --white:#fff;
  --photo-a:#3b4250;
  --photo-b:#7a8fb0;
}
*{margin:0;padding:0;box-sizing:border-box}
html,body{width:846px;height:1200px;overflow:hidden;background:var(--white)}
.flyer{position:relative;width:846px;height:1200px;overflow:hidden;color:var(--ink);font-family:"Inter",Helvetica,sans-serif}
.center{position:absolute;left:0;width:846px;text-align:center}
.brand{position:absolute;top:18px;left:0;width:846px;display:flex;justify-content:center;align-items:center;gap:14px}
.brand-mark{width:64px;height:64px;border-radius:50%;background:var(--plum)}
.brand-name{font-family:"Playfair Display",Georgia,serif;font-weight:500;font-size:46px;letter-spacing:5px;color:var(--plum)}
.opening{top:112px;font-family:"Archivo Black",Arial,sans-serif;font-size:46px;letter-spacing:0.5px}
.headline{top:200px;font-family:"Courier Prime","Courier New",monospace;font-weight:700;font-size:61px;line-height:63px;letter-spacing:-0.5px}
.intro{top:476px;font-weight:300;font-size:27px;line-height:36.5px;letter-spacing:-0.3px}
.offer{top:693px;font-weight:300;font-size:27px;line-height:37px;letter-spacing:-0.3px}
.now{top:763px;font-family:"Archivo Black",Arial,sans-serif;font-size:46px}
.date{top:818px;font-weight:700;font-size:28px;line-height:36px}
.date .light{font-weight:400}
.badge{position:absolute;border-radius:50%;background:var(--orange);color:var(--white);font-family:"Oswald",Arial,sans-serif;font-weight:600;text-align:center}
.badge-inner{position:absolute;left:0;top:0;width:100%;height:100%;transform:rotate(-10deg);display:flex;flex-direction:column;justify-content:center;align-items:center;line-height:1}
.badge .new{font-size:30px}
.badge .pct{font-size:108px;letter-spacing:-3px;line-height:0.95}
.badge .all{font-size:32px}
.badge-top{left:-25px;top:-65px;width:188px;height:188px}
.badge-top .badge-inner{justify-content:flex-end;padding-bottom:28px}
.badge-top .pct{font-size:96px}
.badge-right{left:629px;top:553px;width:236px;height:236px}
.badge-left{left:-26px;top:968px;width:240px;height:240px}
.gallery{position:absolute;top:943px;left:53px;display:flex;gap:23px}
.photo{width:172px;height:209px;background:linear-gradient(160deg,var(--photo-b) 0%,var(--photo-a) 70%)}
</style>
</head>
<body>
<main class="flyer">
  <div class="badge badge-top"><div class="badge-inner"><span class="pct">20%</span><span class="all">AUF ALLES</span></div></div>

  <header class="brand">
    <span class="brand-name">feinKragen</span>
    <span class="brand-mark"></span>
  </header>

  <h1 class="center opening">NEUERÖFFNUNG!</h1>

  <p class="center headline">Jetzt endlich auch in<br>Oberkochen, Mode für<br>den anspruchsvollen<br>Mann von heute.</p>

  <p class="center intro">Wir bieten Marken Hemden und Accessoires<br>unter anderem von den Herstellern<br>Faltenmeister, Lumira und Veltrano.<br>In unserem Ladengeschäft<br>sowie online in unserem Shop.</p>

  <p class="center offer">NUTZEN SIE UNSERE<br>NEUERÖFFNUNGSRABATTE,</p>
  <p class="center now">JETZT!</p>
  <p class="center date">AM SAMSTAG, 01. APRIL 09:00-16:00 UHR<br>20% AUF ALLES <span class="light">- KEIN APRILSCHERZ!</span></p>

  <div class="badge badge-right"><div class="badge-inner"><span class="new">NEU!</span><span class="pct">-20%</span><span class="all">AUF ALLES</span></div></div>

  <section class="gallery">
    <div class="photo" role="img" aria-label="Mann im dunklen Anzug mit blauem Hemd richtet seine rote Krawatte"></div>
    <div class="photo" role="img" aria-label="Mann im dunklen Anzug mit blauem Hemd richtet seine rote Krawatte"></div>
    <div class="photo" role="img" aria-label="Mann im dunklen Anzug mit blauem Hemd richtet seine rote Krawatte"></div>
    <div class="photo" role="img" aria-label="Mann im Anzug mit roter Krawatte, daneben eine Frau im roten Kleid"></div>
  </section>

  <div class="badge badge-left"><div class="badge-inner"><span class="new">NEU!</span><span class="pct">-20%</span><span class="all">AUF ALLES</span></div></div>
</main>
</body>
</html>
```